Family owned plumbing contractor needs eye catching business card design

Business cards that are unique, eye catching, and provide customers with general company information, such as name, address, phone number, website, employee name/title, cell phone #, & email address. We are transitioning to a new logo that utilizes a more retro feel, so we are interested in seeing some cool old school designs in the mix. We are liking the dark background on some of the samples on this website. If that is workable with our artwork, we would like to see that incorporated into the design.
Contact Information for Business Card
Copperline Pipeworks, Inc.
www.copperlinepipeworks.example
(555) 392-7068 phone
Nevada License #64205
California License #5810473
Dale Wrennick, President
(555) 618-9032 cell
dale@copperlinepipeworks.example
Residential * Commercial * Service
Requirements
Must have
- The business card details listed above & logo provided.
Nice to have
- I made some notes about color options in the description.

```html
<!DOCTYPE html>
<html lang="en">
<head>
<meta charset="utf-8">
<title>Copperline Pipeworks – Business Card</title>
<link rel="stylesheet" href="https://fonts.googleapis.com/css2?family=Marcellus+SC&family=Montserrat:wght@400;500&display=swap">
<style>
  :root {
    --backdrop: #9a9a9a;
    --front-blue: #416a84;
    --back-blue: #50778f;
    --teal: #7fc6b9;
    --white: #ffffff;
    --soft-white: #eef3f5;
  }
  * { box-sizing: border-box; margin: 0; padding: 0; }
  html, body {
    width: 1200px; height: 1200px; overflow: hidden;
    background: var(--backdrop);
  }
  .canvas { position: relative; width: 1200px; height: 1200px; }
  .card {
    position: absolute; left: 195px; width: 810px; height: 486px;
    color: var(--white); overflow: hidden;
  }
  .card-front { top: 66px; background: var(--front-blue); }
  .card-back { top: 614px; background: var(--back-blue); }

  .brand-mark {
    position: absolute; display: flex; align-items: center; justify-content: center;
    font-family: "Marcellus SC", serif; color: var(--white); white-space: nowrap;
  }
  .brand-dot { border-radius: 50%; background: var(--teal); flex: none; }

  .front-mark { left: 0; right: 0; top: 150px; gap: 18px; font-size: 40px; }
  .front-mark .brand-dot { width: 64px; height: 64px; }

  .front-name {
    position: absolute; left: 0; right: 0; top: 372px; text-align: center;
    font-family: "Marcellus SC", serif; font-size: 30px; letter-spacing: 1px;
  }
  .front-tagline {
    position: absolute; left: 0; right: 0; top: 426px; text-align: center;
    font-family: "Marcellus SC", serif; font-size: 14px; letter-spacing: 1px;
  }

  .band { position: absolute; left: 0; width: 100%; background: var(--teal); }
  .band-top { top: 0; height: 34px; }
  .band-bottom { top: 453px; height: 33px; display: flex; align-items: center; justify-content: center;
    font-family: Montserrat, sans-serif; font-size: 13px; }

  .back-mark {
    left: 40px; width: 340px; top: 196px; flex-direction: column; gap: 12px;
    font-size: 22px;
  }
  .back-mark .brand-dot { width: 50px; height: 50px; }
  .back-company {
    position: absolute; left: 40px; width: 340px; top: 349px; text-align: center;
    font-family: "Marcellus SC", serif; font-size: 15px; letter-spacing: .5px;
  }

  .contact { position: absolute; left: 455px; top: 98px; font-family: Montserrat, sans-serif; color: var(--soft-white); }
  .person-name { font-family: "Marcellus SC", serif; font-size: 36px; color: var(--white); line-height: 1.1; letter-spacing: 1px; }
  .person-title { font-size: 14px; margin-top: 2px; }
  .contact-lines { list-style: none; margin-top: 46px; font-size: 14px; }
  .contact-lines li { height: 27px; }
  .contact-lines .label { font-weight: 500; font-size: 12px; }
  .licenses { margin-top: 36px; font-size: 14px; line-height: 18px; }
</style>
</head>
<body>
<main class="canvas">
  <section class="card card-front" aria-label="Business card front">
    <div class="brand-mark front-mark">
      <span class="brand-dot"></span>
      <span>Copperline Pipeworks, Inc.</span>
    </div>
    <h1 class="front-name">Copperline Pipeworks, Inc.</h1>
    <p class="front-tagline">Residential * Commercial * Service</p>
  </section>

  <section class="card card-back" aria-label="Business card back">
    <div class="band band-top"></div>
    <div class="brand-mark back-mark">
      <span class="brand-dot"></span>
      <span>Copperline Pipeworks, Inc.</span>
    </div>
    <p class="back-company">Copperline Pipeworks, Inc.</p>

    <div class="contact">
      <h2 class="person-name">Dale Wrennick</h2>
      <p class="person-title">President</p>
      <ul class="contact-lines">
        <li><span class="label">C:</span> (555) 618-9032</li>
        <li><span class="label">P:</span> (555) 392-7068</li>
        <li><span class="label">E:</span> dale@copperlinepipeworks.example</li>
        <li>www.copperlinepipeworks.example</li>
      </ul>
      <p class="licenses">Nevada License #64205<br>California License #5810473</p>
    </div>

    <div class="band band-bottom">www.copperlinepipeworks.example</div>
  </section>
</main>
</body>
</html>
```